LA's Newest HEMP Facial Oil and Body Oil Packaging Project

We need a packaging concept for a Hemp based facial oil and body oil. We need label design for the bottle and carton graphics. I am attaching a few reference photos. The target demographic is women between 17-35 year old. Products need to be able to stand out in crowded stores with clear calls to action.
1oz Dropper Bottle with Unit Carton - Hemp Facial Oil
4oz PET Bottle with Unit Carton - SOLA + PETAL Facial Oil

```html
<!DOCTYPE html>
<html lang="en">
<head>
<meta charset="utf-8">
<title>Sola + Petal Facial Oil – Carton and Label</title>
<link rel="stylesheet" href="https://fonts.googleapis.com/css2?family=Oswald:wght@400&family=Tinos:wght@700&display=swap">
<style>
  :root {
    --backdrop: #efe2da;
    --rose-red: #e8404f;
    --rose-pink: #f07a84;
    --badge-black: #231c1c;
    --badge-gold: #e6c77a;
    --carton-gold-top: #c9a06e;
    --carton-gold-bottom: #b98c5a;
    --label-gold-top: #f2eab0;
    --label-gold-bottom: #ddd08a;
    --leaf-tone: #e9d6c2;
    --ink: #231c1c;
  }
  * { box-sizing: border-box; margin: 0; padding: 0; }
  html, body { width: 1200px; height: 900px; overflow: hidden; }
  body {
    background: var(--backdrop);
    position: relative;
    font-family: "Tinos", "Times New Roman", serif;
  }
  .panel { position: absolute; overflow: hidden; }
  .carton-front { left: 250px; top: 50px; width: 280px; height: 800px; }
  .bottle-label { left: 650px; top: 190px; width: 300px; height: 520px; }
  .rose-pattern {
    position: absolute; inset: 0;
    background: radial-gradient(circle at 40% 35%, var(--rose-pink), var(--rose-red) 75%);
  }
  .brand-seal {
    position: absolute; left: 50%; transform: translateX(-50%);
    border-radius: 50%;
    background: var(--badge-black);
    display: flex; flex-direction: column; align-items: center; justify-content: center;
    font-family: "Oswald", "Arial Narrow", sans-serif;
    font-weight: 400;
    color: var(--badge-gold);
    line-height: 1.05;
    text-align: center;
  }
  .carton-front .brand-seal { top: 230px; width: 170px; height: 170px; font-size: 34px; }
  .bottle-label .brand-seal { top: 70px; width: 180px; height: 180px; font-size: 36px; }
  .brand-seal .brand-join, .brand-seal .brand-second { font-size: 0.62em; }
  .info-panel {
    position: absolute; left: 50%; transform: translateX(-50%);
    display: flex; flex-direction: column; align-items: center;
  }
  .carton-front .info-panel {
    bottom: 0; width: 172px; height: 320px;
    background: linear-gradient(var(--carton-gold-top), var(--carton-gold-bottom));
    padding-top: 50px;
  }
  .bottle-label .info-panel {
    bottom: 0; width: 180px; height: 220px;
    background: linear-gradient(var(--label-gold-top), var(--label-gold-bottom));
    padding-top: 30px;
  }
  .product-type { font-size: 16px; color: var(--ink); letter-spacing: 0.5px; white-space: nowrap; }
  .leaf-mark {
    width: 70px; height: 70px; margin-top: 26px;
    background: var(--leaf-tone); border-radius: 50%; opacity: .8;
  }
  .bottle-label .leaf-mark { margin-top: 16px; width: 60px; height: 60px; background: #f5f2e6; }
  .volume { font-size: 10px; color: var(--ink); margin-top: 48px; white-space: nowrap; }
  .bottle-label .volume { margin-top: 24px; }
  .base-band {
    position: absolute; left: 0; right: 0; bottom: 0;
    background: var(--badge-black);
  }
  .carton-front .base-band { height: 26px; }
  .bottle-label .base-band { height: 12px; }
</style>
</head>
<body>
  <section class="panel carton-front">
    <div class="rose-pattern" role="img" aria-label="Line-drawn red and pink rose pattern covering the carton"></div>
    <div class="brand-seal">
      <span class="brand-first">SOLA</span>
      <span class="brand-join">+</span>
      <span class="brand-second">PETAL</span>
    </div>
    <div class="info-panel">
      <p class="product-type">~ FACIAL OIL ~</p>
      <div class="leaf-mark" role="img" aria-label="Hemp leaf illustration"></div>
      <p class="volume">1 FL OZ (30ML)</p>
      <div class="base-band"></div>
    </div>
  </section>

  <section class="panel bottle-label">
    <div class="rose-pattern" role="img" aria-label="Line-drawn red and pink rose pattern covering the bottle label"></div>
    <div class="brand-seal">
      <span class="brand-first">SOLA</span>
      <span class="brand-join">+</span>
      <span class="brand-second">PETAL</span>
    </div>
    <div class="info-panel">
      <p class="product-type">~ FACIAL OIL ~</p>
      <div class="leaf-mark" role="img" aria-label="Hemp leaf illustration"></div>
      <p class="volume">1 FL OZ (30ML)</p>
      <div class="base-band"></div>
    </div>
  </section>
</body>
</html>
```